Business Bench-marking brochure

Create a single page flyer for an account firm to advertise their Business Bench-marking product offering.

Style should follow new corporate image in development as per attached website psd.

The client likes the logo to always be on the RIGHT of publications.

Target Market(s)

Small - Medium sucessfully Business

Industry/Entity Type

Business

Colors
eb1f27

Requirements
Nice to have
• The client would like an image of a scales with Apples on both sides to be used -the idea being "comparing apples to apples"

```html
<!DOCTYPE html>
<html lang="en">
<head>
<meta charset="utf-8">
<title>How Does Your Business Compare? – Harlow Business Consulting</title>
<link href="https://fonts.googleapis.com/css2?family=Roboto:wght@300;400;700;900&display=swap" rel="stylesheet">
<style>
  :root {
    --brand-red: #d7141d;
    --ink: #111111;
    --body-ink: #2b2b2b;
    --paper: #ffffff;
    --backdrop: #ece9e4;
    --photo-top: #f3f3f1;
    --photo-bottom: #d4d6d1;
  }
  * { margin: 0; padding: 0; box-sizing: border-box; }
  html, body { width: 954px; height: 1200px; overflow: hidden; }
  body {
    background: var(--backdrop);
    font-family: 'Roboto', Arial, sans-serif;
    color: var(--body-ink);
    position: relative;
  }
  .flyer {
    position: absolute;
    left: 58px; top: 58px;
    width: 838px; height: 1084px;
    background: var(--paper);
  }
  .headline {
    position: absolute;
    left: 64px; top: 74px;
    font-weight: 300;
    font-size: 63px;
    line-height: 70px;
    color: var(--ink);
    letter-spacing: 0.3px;
  }
  .headline strong { font-weight: 900; }
  .intro {
    position: absolute;
    left: 63px; top: 231px;
    width: 236px;
  }
  .intro .lead {
    color: var(--brand-red);
    font-weight: 700;
    font-size: 15px;
    line-height: 18px;
    margin-bottom: 18px;
  }
  .intro .body {
    font-weight: 300;
    font-size: 15px;
    line-height: 17.5px;
    color: var(--body-ink);
  }
  .benefits {
    position: absolute;
    left: 332px; top: 239px;
    width: 480px;
  }
  .benefits h2 {
    color: var(--brand-red);
    font-weight: 700;
    font-size: 15px;
    margin-bottom: 10px;
  }
  .benefits ul { list-style: none; }
  .benefits li {
    font-weight: 300;
    font-size: 15px;
    line-height: 18px;
    margin-bottom: 11.5px;
    display: flex;
    align-items: center;
    gap: 5px;
  }
  .benefits li svg { flex: none; }
  .cta {
    position: absolute;
    left: 332px; top: 441px;
    width: 480px;
    font-weight: 300;
    font-size: 15px;
    line-height: 17.5px;
  }
  .cta p + p { margin-top: 6px; }
  .hero-image {
    position: absolute;
    left: 30px; top: 572px;
    width: 505px; height: 435px;
    background: linear-gradient(180deg, var(--photo-top) 0%, var(--photo-bottom) 100%);
  }
  .brand {
    position: absolute;
    left: 556px; top: 926px;
    color: var(--ink);
  }
  .brand .name {
    font-weight: 900;
    font-size: 44px;
    line-height: 44px;
    letter-spacing: 0.5px;
  }
  .brand .sub {
    font-weight: 400;
    font-size: 16px;
    letter-spacing: 0.3px;
    margin-top: 2px;
  }
  .contact {
    position: absolute;
    left: 41px; top: 1043px;
    width: 770px;
    display: flex;
    align-items: center;
    font-size: 14.5px;
    color: var(--ink);
  }
  .contact .label { font-weight: 700; margin-right: 22px; }
  .contact .item { display: flex; align-items: center; gap: 6px; margin-right: 24px; }
  .contact .item:last-child { margin-right: 0; }
</style>
</head>
<body>
  <main class="flyer">
    <h1 class="headline">HOW DOES YOUR<br>BUSINESS <strong>COMPARE</strong>?</h1>

    <section class="intro">
      <p class="lead">Ever wondered how your business compares to your competitors?</p>
      <p class="lead">Why you may be struggling to make a profit while other businesses in your industry seem to have it all figured out?</p>
      <p class="body">By capturing the financial information and KPIs of your business we can compare your business to those within your industry.&nbsp; This enables you to be armed with the knowledge of how you can take corrective action by making informed decisions to save money and significantly enhance your overall performance</p>
    </section>

    <section class="benefits">
      <h2>Benchmarking helps you:</h2>
      <ul>
        <li><svg width="14" height="12" viewBox="0 0 14 12"><path d="M1 1l5 5-5 5M6 1l5 5-5 5" fill="none" stroke="var(--brand-red)" stroke-width="1.6"/></svg>Identify where you can reduce costs and improve efficiencies</li>
        <li><svg width="14" height="12" viewBox="0 0 14 12"><path d="M1 1l5 5-5 5M6 1l5 5-5 5" fill="none" stroke="var(--brand-red)" stroke-width="1.6"/></svg>Determine the productivity of your employees</li>
        <li><svg width="14" height="12" viewBox="0 0 14 12"><path d="M1 1l5 5-5 5M6 1l5 5-5 5" fill="none" stroke="var(--brand-red)" stroke-width="1.6"/></svg>Highlight opportunities for improvement and innovative practices</li>
        <li><svg width="14" height="12" viewBox="0 0 14 12"><path d="M1 1l5 5-5 5M6 1l5 5-5 5" fill="none" stroke="var(--brand-red)" stroke-width="1.6"/></svg>Discover opportunities for making your business more competitive</li>
      </ul>
    </section>

    <section class="cta">
      <p>To ensure your business is operating at its peak performance, call Harlow Business Consulting for your detailed benchmark report.</p>
      <p>Full analysis of your financial statements, including KPIs, along with a meeting with Nadia Harlow to identify areas to improve to help your business prosper.</p>
    </section>

    <div class="hero-image" role="img" aria-label="Photo: balance scale with a green apple on one pan and a red apple on the other, comparing apples to apples"></div>

    <div class="brand">
      <div class="name">HARLOW</div>
      <div class="sub">BUSINESS CONSULTING</div>
    </div>

    <footer class="contact">
      <span class="label">Contact Details:</span>
      <span class="item">
        <svg width="16" height="11" viewBox="0 0 16 11"><rect x="0.5" y="0.5" width="15" height="10" fill="var(--brand-red)"/><path d="M0.5 0.5l7.5 6 7.5-6" fill="none" stroke="#fff" stroke-width="1.2"/></svg>
        admin@harlowconsulting.com.au
      </span>
      <span class="item">
        <svg width="10" height="16" viewBox="0 0 10 16"><rect x="0.5" y="0.5" width="9" height="15" rx="1.5" fill="var(--brand-red)"/><rect x="2" y="2.5" width="6" height="8" fill="#fff"/></svg>
        02 5550 1847
      </span>
      <span class="item">
        <svg width="15" height="15" viewBox="0 0 16 16"><g fill="none" stroke="var(--brand-red)" stroke-width="1.3"><circle cx="8" cy="8" r="7"/><ellipse cx="8" cy="8" rx="3" ry="7"/><path d="M1 8h14M2.5 4h11M2.5 12h11"/></g></svg>
        www.harlowconsulting.com.au
      </span>
    </footer>
  </main>
</body>
</html>
```